Landing page for a cyber security service provider called 'Lumen Grove'

The client is a new cyber security company in need of a website landing page at lumengrove.example.

Their visual identity is modern, playful, clean and uncluttered and represents innovation, connectivity and approachability.

The company logo is provided in black (attached) but the client is open to changing the colour to align with the new website design.

The landing page needs to contain:
- A call to action with a 'Get Started' button
-Links to blank 'How it works', 'Products', 'Pricing', 'About Us' and 'Contact Us' pages (that we'll fill out later)

Target Market(s)

Medium to large businesses who probably don't understand cyber / cyber security but need their business to be protected.

Industry/Entity Type

Cyber Security

Coding

Coded - Design and coding required

Number of Pages Required

1 page

Font styles to use
Sans Serif
Other font styles liked:
• Helvetica

Requirements
Nice to have
• Hero banner at the top of the landing page.
Should not have
• Should not look like a traditional cyber / cyber security design (eg no dark blue/ black, red/black colour combinations). Please no military styles (eg no shields, cannons, swords, guns)

```html
<!DOCTYPE html>
<html lang="en">
<head>
<meta charset="utf-8">
<title>Lumen Grove — How Secure Is Your Data</title>
<link href="https://fonts.googleapis.com/css2?family=Montserrat:wght@500;600;700;800&family=Poppins:wght@400;500;600&display=swap" rel="stylesheet">
<style>
:root{
  --red:#d2132b;
  --ink:#1c1c1c;
  --text:#3d3d3d;
  --muted:#6b6b6b;
  --paper:#ffffff;
  --panel:#e4e4e4;
  --band-top:#7d8289;
  --band-bottom:#676c73;
  --sky-light:#e3f1f9;
  --sky-mid:#a9d3ec;
  --sky-deep:#6fb1d9;
  --teal-light:#def4f2;
  --teal-mid:#9fd9d4;
  --teal-deep:#62b8b3;
  --heading:'Montserrat',Arial,sans-serif;
  --body:'Poppins',Arial,sans-serif;
}
*{box-sizing:border-box;margin:0;padding:0}
html,body{width:1200px;height:4950px;overflow:hidden}
body{position:relative;background:var(--paper);font-family:var(--body);color:var(--text)}
a{text-decoration:none;color:inherit}

/* header */
.hero-bg{position:absolute;left:0;top:0;width:1200px;height:770px;background:linear-gradient(180deg,#efefef 0%,#f6f6f6 45%,#fff 100%)}
.brand{position:absolute;display:flex;align-items:center;gap:8px;font-family:var(--heading);font-weight:700;color:var(--red);white-space:nowrap}
.brand-dot{width:14px;height:14px;border-radius:50%;background:var(--red)}
.site-brand{left:186px;top:42px;font-size:20px}
.nav{position:absolute;top:48px;left:0;font-family:var(--body);font-size:15px;color:#222}
.nav a{position:absolute;white-space:nowrap}
.nav .active{color:var(--red)}
.btn-contact{position:absolute;left:930px;top:42px;width:116px;height:36px;border-radius:18px;background:var(--red);color:#fff;font-size:13px;display:flex;align-items:center;justify-content:center}

/* photo placeholders */
.photo{position:absolute;border-radius:50%}
.ring{position:absolute;border:2px solid var(--red);border-radius:50%}
.hero-photo{left:-55px;top:135px;width:650px;height:650px;background:radial-gradient(circle at 45% 55%,var(--sky-light) 0%,var(--sky-mid) 45%,var(--sky-deep) 100%)}

.hero-line{position:absolute;left:523px;top:303px;width:90px;height:3px;background:var(--red)}
.hero-line::after{content:"";position:absolute;left:-6px;top:-3px;width:9px;height:9px;border-radius:50%;background:var(--red)}
.hero-title{position:absolute;left:630px;top:262px;font-family:var(--heading);font-weight:700;font-size:52px;line-height:58px;color:var(--ink);white-space:nowrap}
.hero-title .accent{color:var(--red)}
.hero-sub{position:absolute;left:638px;top:390px;font-family:var(--heading);font-weight:500;font-size:27px;line-height:31px;color:#333;white-space:nowrap}
.hero-text{position:absolute;left:638px;top:466px;width:410px;font-size:12.5px;line-height:23px;color:#444}
.btn-outline{position:absolute;display:flex;align-items:center;justify-content:center;border:2px solid var(--red);border-radius:22px;color:var(--red);font-family:var(--heading);font-weight:600;background:#fff;white-space:nowrap}
.hero-cta{left:640px;top:532px;width:152px;height:40px;font-size:16px;font-family:var(--body);font-weight:500}

/* sections */
.section-title{position:absolute;left:0;width:1200px;text-align:center;font-family:var(--heading);font-weight:700;color:var(--ink)}
.underline{position:absolute;left:576px;width:48px;height:4px;background:var(--red);border-radius:2px}
.intro{position:absolute;left:200px;width:800px;text-align:center;font-size:15px;line-height:23px;color:#333}

.connectors{position:absolute;left:0;top:0;width:1200px;height:4950px;pointer-events:none}

.gear{position:absolute;width:290px;height:290px}
.gear-bg{position:absolute;left:0;top:0;filter:drop-shadow(0 10px 18px rgba(0,0,0,.12))}
.gear-body{position:absolute;left:0;top:0;width:290px;height:290px;display:flex;flex-direction:column;align-items:center;justify-content:center;text-align:center;padding-top:8px}
.gear-icon{width:40px;height:40px;margin-bottom:10px;flex:none}
.gear h3{font-family:var(--heading);font-weight:600;font-size:15px;color:var(--ink);letter-spacing:.2px}
.gear p{font-size:10px;line-height:15px;color:#444;width:180px;margin-top:4px}
.chev{width:30px;height:30px;border-radius:50%;border:1.5px solid #888;margin-top:14px;display:flex;align-items:center;justify-content:center}
.gear.featured h3,.gear.featured p{color:#fff}
.gear.featured .chev{border-color:#fff}

.service-title{position:absolute;font-family:var(--heading);font-size:30px;line-height:36px;white-space:nowrap}
.service-title .accent{color:var(--red);font-weight:700;display:block}
.service-title .rest{color:var(--ink);font-weight:500;display:block}
.service-text{position:absolute;font-size:15px;line-height:23px;color:#333}
.btn-small{width:160px;height:42px;font-size:13px}

/* blogs */
.blog{position:absolute;top:3406px;width:305px;height:388px;background:#fff;box-shadow:0 4px 14px rgba(0,0,0,.09)}
.blog-photo{height:202px;width:100%}
.blog-body{padding:16px 30px 0 30px}
.blog-date{font-family:var(--heading);font-weight:600;font-size:12px;color:var(--red)}
.blog h4{font-family:var(--heading);font-weight:700;font-size:15px;line-height:24px;color:var(--ink);margin-top:6px}
.blog p{font-size:9px;line-height:14px;color:#777;margin-top:8px}

/* trust */
.city-band{position:absolute;left:0;top:4117px;width:1200px;height:519px;background:linear-gradient(180deg,var(--band-top) 0%,var(--band-bottom) 100%)}
.trust{position:absolute;left:125px;top:3911px;width:948px;height:271px;background:var(--panel);border-radius:50px 90px 50px 50px}
.trust h2{position:absolute;top:60px;width:100%;text-align:center;font-family:var(--heading);font-weight:600;font-size:24px;color:#333;letter-spacing:.4px}
.partner{position:absolute;top:120px;width:156px;height:71px;background:#fff;box-shadow:0 2px 6px rgba(0,0,0,.08);display:flex;align-items:center;justify-content:center;font-family:var(--heading);font-weight:700;font-size:15px;color:#333}
.cta-title{position:absolute;left:0;width:1200px;text-align:center;font-family:var(--heading);color:#fff;font-size:31px;line-height:36px}
.cta-text{position:absolute;left:270px;top:4371px;width:660px;text-align:center;color:#fff;font-size:14px;line-height:23px}
.btn-white{position:absolute;left:512px;top:4442px;width:171px;height:42px;border-radius:21px;background:#fff;color:var(--red);font-family:var(--heading);font-weight:700;font-size:14px;display:flex;align-items:center;justify-content:center}

/* footer */
.footer-brand{left:248px;top:4742px;font-size:22px}
.social{position:absolute;top:4805px;width:24px;height:24px;border-radius:50%;border:1.5px solid #555}
.foot-col{position:absolute;top:4705px;width:200px}
.foot-col h5{font-family:var(--heading);font-weight:700;font-size:12px;color:#222;letter-spacing:.3px;padding-bottom:6px;border-bottom:1px solid #c9c9c9;width:110px}
.foot-col a{position:absolute;left:6px;font-size:11px;color:#222;white-space:nowrap}
.foot-col a.active{color:var(--red)}
.contact-row{position:absolute;left:0;display:flex;align-items:center;gap:10px;white-space:nowrap}
.contact-icon{width:22px;height:22px;border-radius:50%;background:var(--red);display:flex;align-items:center;justify-content:center;flex:none}
.contact-row small{display:block;font-size:9px;color:#666}
.contact-row span{display:block;font-size:12px;color:#111}
.copyright{position:absolute;left:0;top:4900px;width:1200px;height:50px;background:#ebebeb;display:flex;align-items:center;justify-content:center;font-size:12px;color:#333}
</style>
</head>
<body>

<svg width="0" height="0" style="position:absolute">
  <defs>
    <g id="gear-shape">
      <circle cx="0" cy="0" r="120"/>
      <rect x="-30" y="-143" width="60" height="50" rx="14"/>
      <rect x="-30" y="-143" width="60" height="50" rx="14" transform="rotate(45)"/>
      <rect x="-30" y="-143" width="60" height="50" rx="14" transform="rotate(90)"/>
      <rect x="-30" y="-143" width="60" height="50" rx="14" transform="rotate(135)"/>
      <rect x="-30" y="-143" width="60" height="50" rx="14" transform="rotate(180)"/>
      <rect x="-30" y="-143" width="60" height="50" rx="14" transform="rotate(225)"/>
      <rect x="-30" y="-143" width="60" height="50" rx="14" transform="rotate(270)"/>
      <rect x="-30" y="-143" width="60" height="50" rx="14" transform="rotate(315)"/>
    </g>
  </defs>
</svg>

<!-- Header & hero -->
<div class="hero-bg"></div>
<a class="brand site-brand" href="#"><span class="brand-dot"></span>Lumen Grove</a>
<nav class="nav">
  <a class="active" href="#" style="left:427px">Home</a>
  <a href="#how-it-works" style="left:502px">How it works</a>
  <a href="#products" style="left:625px">Products</a>
  <a href="#pricing" style="left:721px">Pricing</a>
  <a href="#about" style="left:800px">About Us</a>
</nav>
<a class="btn-contact" href="#contact">Contact Us</a>

<div class="photo hero-photo" role="img" aria-label="City skyline with glowing data light beams"></div>
<div class="hero-line"></div>
<h1 class="hero-title">HOW SECURE IS<br><span class="accent">YOUR DATA</span></h1>
<p class="hero-sub">THOROUGH AND EFFECTIVE<br>SECURITY CONTROLS</p>
<p class="hero-text">Lumen Grove information security professionals assist customers with understanding the effectiveness of preventive</p>
<a class="btn-outline hero-cta" href="#get-started">Get Started</a>

<!-- Connectors -->
<svg class="connectors" viewBox="0 0 1200 4950" aria-hidden="true">
  <g fill="none" stroke="#d2132b" stroke-width="2">
    <polyline points="598,962 598,1008 321,1008 321,1034"/>
    <polyline points="606,962 606,1034"/>
    <polyline points="614,962 614,1008 877,1008 877,1034"/>
    <polyline points="610,1369 610,1490 283,1490 283,1524"/>
    <polyline points="360,1869 360,1954 685,1954 685,2066"/>
    <polyline points="673,2513 673,2617 346,2617 346,2706"/>
    <polyline points="271,3119 271,3223 598,3223 598,3304"/>
  </g>
  <g fill="#fff" stroke="#d2132b" stroke-width="2">
    <circle cx="321" cy="1039" r="5"/>
    <circle cx="877" cy="1039" r="5"/>
    <circle cx="283" cy="1529" r="5"/>
    <circle cx="685" cy="2071" r="5"/>
    <circle cx="346" cy="2711" r="5"/>
    <circle cx="598" cy="3309" r="5"/>
  </g>
</svg>

<!-- What we do -->
<h2 class="section-title" style="top:822px;font-size:32px">WHAT WE DO</h2>
<div class="underline" style="top:869px"></div>
<p class="intro" style="top:890px">Lumen Grove information security professionals assist customers with understanding the effectiveness of preventive, detective and corrective security controls by testing and analyzing networks, applications</p>

<div class="gear" style="left:157px;top:1043px">
  <svg class="gear-bg" width="290" height="290" viewBox="-145 -145 290 290"><use href="#gear-shape" fill="#fff"/></svg>
  <div class="gear-body">
    <svg class="gear-icon" viewBox="0 0 40 40" fill="none" stroke="#222" stroke-width="2"><rect x="10" y="18" width="20" height="15" rx="2"/><path d="M14 18v-5a6 6 0 0 1 12 0v5"/></svg>
    <h3>CYBER SECURITY</h3>
    <p>Lorem ipsum dolor sit amet, consectetur adipiscing elitsed do</p>
    <span class="chev"><svg width="12" height="8" viewBox="0 0 12 8"><path d="M1 1l5 5 5-5" fill="none" stroke="#888" stroke-width="1.6"/></svg></span>
  </div>
</div>
<div class="gear featured" style="left:459px;top:1043px">
  <svg class="gear-bg" width="290" height="290" viewBox="-145 -145 290 290"><use href="#gear-shape" fill="#d2132b"/></svg>
  <div class="gear-body">
    <svg class="gear-icon" viewBox="0 0 40 40" fill="none" stroke="#fff" stroke-width="2"><circle cx="20" cy="14" r="6"/><path d="M8 34c0-7 5-11 12-11s12 4 12 11"/></svg>
    <h3>CONSULTING</h3>
    <p>Lorem ipsum dolor sit amet, consectetur adipiscing elitsed do</p>
    <span class="chev"><svg width="12" height="8" viewBox="0 0 12 8"><path d="M1 1l5 5 5-5" fill="none" stroke="#fff" stroke-width="1.6"/></svg></span>
  </div>
</div>
<div class="gear" style="left:759px;top:1043px">
  <svg class="gear-bg" width="290" height="290" viewBox="-145 -145 290 290"><use href="#gear-shape" fill="#fff"/></svg>
  <div class="gear-body">
    <svg class="gear-icon" viewBox="0 0 40 40" fill="none" stroke="#222" stroke-width="2"><circle cx="20" cy="20" r="7"/><path d="M20 6v5M20 29v5M6 20h5M29 20h5"/></svg>
    <h3>MANAGEMENT</h3>
    <p>Lorem ipsum dolor sit amet, consectetur adipiscing elitsed do</p>
    <span class="chev"><svg width="12" height="8" viewBox="0 0 12 8"><path d="M1 1l5 5 5-5" fill="none" stroke="#888" stroke-width="1.6"/></svg></span>
  </div>
</div>

<!-- Regulatory -->
<h2 class="service-title" style="left:117px;top:1564px"><span class="accent">REGULATORY</span><span class="rest">COMPLIANCE SERVICES</span></h2>
<p class="service-text" style="left:117px;top:1652px;width:450px">Led by industry experts, Lumen Grove provides compliance assessment services for a number of industry regulatory compliance requirements, including the Regional Financial Standards Council (RFSC)</p>
<a class="btn-outline btn-small" href="#" style="left:117px;top:1773px">LEARN MORE</a>
<div class="ring" style="left:660px;top:1395px;width:636px;height:636px"></div>
<div class="photo" role="img" aria-label="Hand touching a glowing digital compliance dashboard" style="left:676px;top:1412px;width:604px;height:604px;background:radial-gradient(circle at 45% 45%,var(--sky-light) 0%,var(--sky-mid) 50%,var(--sky-deep) 100%)"></div>

<!-- Remediation -->
<div class="ring" style="left:-95px;top:1985px;width:612px;height:612px"></div>
<div class="photo" role="img" aria-label="Close view of glowing circuit board traces" style="left:-70px;top:2003px;width:585px;height:585px;background:radial-gradient(circle at 55% 45%,var(--teal-light) 0%,var(--teal-mid) 50%,var(--teal-deep) 100%)"></div>
<h2 class="service-title" style="left:604px;top:2114px"><span class="accent">REMEDIATION</span><span class="rest">SERVICES</span></h2>
<p class="service-text" style="left:606px;top:2206px;width:470px">Lumen Grove can assist with planning, prioritizing and managing process and infrastructure upgrades to achieve compliance with industry regulatory standards or best practices.  As part of our assessment services, we help identify and prioritize specific cyber security risks.</p>
<a class="btn-outline btn-small" href="#" style="left:604px;top:2354px">LEARN MORE</a>

<!-- Security management -->
<h2 class="service-title" style="left:125px;top:2791px"><span class="accent">SECURITY MANAGEMENT &amp;</span><span class="rest">STAFF AUGMENTATION</span></h2>
<p class="service-text" style="left:127px;top:2877px;width:475px">One of the biggest challenges that organizations face today is recruiting and retaining information security resources and expertise.  Lumen Grove can assist by providing experienced, certified security practitioners and engineers.</p>
<a class="btn-outline btn-small" href="#" style="left:125px;top:3002px">LEARN MORE</a>
<div class="ring" style="left:700px;top:2568px;width:600px;height:600px"></div>
<div class="photo" role="img" aria-label="Hand reaching toward a glowing network of connected points" style="left:722px;top:2583px;width:570px;height:570px;background:radial-gradient(circle at 55% 45%,#ffffff 0%,var(--sky-light) 20%,var(--sky-mid) 60%,var(--sky-deep) 100%)"></div>

<!-- Latest blogs -->
<h2 class="section-title" style="top:3328px;font-size:28px;font-weight:600">LATEST BLOGS</h2>
<div class="underline" style="top:3369px;width:36px;left:582px"></div>

<article class="blog" style="left:125px">
  <div class="blog-photo" role="img" aria-label="Aerial view of city lights" style="background:linear-gradient(160deg,var(--teal-light) 0%,var(--teal-mid) 55%,var(--teal-deep) 100%)"></div>
  <div class="blog-body">
    <div class="blog-date">25 SEPTEMBER</div>
    <h4>Fusce tellus Sed metus augue convallis et vehicula ut</h4>
    <p>Consectetur augue nisi quis lacus ut ac mi quis lacus mollis aliquam curabitur iaculis tempus eros curabitur vel mi sit amet magna malesuada ultrices.</p>
  </div>
</article>
<article class="blog" style="left:448px">
  <div class="blog-photo" role="img" aria-label="Person using a laptop and phone with a security padlock on screen" style="background:linear-gradient(160deg,#eef3f6 0%,#c5d7e2 55%,#9dbacb 100%)"></div>
  <div class="blog-body">
    <div class="blog-date">15 SEPTEMBER</div>
    <h4>Fusce tellus Sed metus augue convallis et vehicula ut</h4>
    <p>Consectetur augue nisi quis lacus ut ac mi quis lacus mollis aliquam curabitur iaculis tempus eros curabitur vel mi sit amet magna malesuada ultrices.</p>
  </div>
</article>
<article class="blog" style="left:769px">
  <div class="blog-photo" role="img" aria-label="Engineer with a laptop in a server room" style="background:linear-gradient(160deg,var(--sky-light) 0%,var(--sky-mid) 55%,var(--sky-deep) 100%)"></div>
  <div class="blog-body">
    <div class="blog-date">15 SEPTEMBER</div>
    <h4>Fusce tellus Sed metus augue convallis et vehicula ut</h4>
    <p>Consectetur augue nisi quis lacus ut ac mi quis lacus mollis aliquam curabitur iaculis tempus eros curabitur vel mi sit amet magna malesuada ultrices.</p>
  </div>
</article>
<a class="btn-outline btn-small" href="#" style="left:523px;top:3821px">LEARN MORE</a>

<!-- Trust & CTA -->
<div class="city-band" role="img" aria-label="Soft city skyline at dusk"></div>
<section class="trust">
  <h2>WE TRUST LUMEN GROVE WITH OUR SECURITY</h2>
  <div class="partner" style="left:63px">Northwind Cards</div>
  <div class="partner" style="left:229px">Valley Health</div>
  <div class="partner" style="left:394px">Corvane</div>
  <div class="partner" style="left:560px">Fieldbank</div>
  <div class="partner" style="left:725px">Tessaro</div>
</section>
<h2 class="cta-title" style="top:4286px;font-weight:700">IMPROVING LIFE</h2>
<h2 class="cta-title" style="top:4322px;font-weight:500">THROUGH CYBER SECURITY</h2>
<p class="cta-text">Anim ad minim veniam, quis nostrud exercitation ullamco laboris nisi ut aliquip ex ea commodo consequat. Duis aute irure dolor in reprehenderit in voluptate</p>
<a class="btn-white" href="#get-started">GET STARTED</a>

<!-- Footer -->
<a class="brand footer-brand" href="#"><span class="brand-dot"></span>Lumen Grove</a>
<span class="social" style="left:255px"></span>
<span class="social" style="left:286px"></span>
<span class="social" style="left:317px"></span>
<span class="social" style="left:348px"></span>

<div class="foot-col" style="left:486px">
  <h5>COMPANY</h5>
  <a class="active" href="#" style="top:44px">Home</a>
  <a href="#how-it-works" style="top:73px">How it works</a>
  <a href="#products" style="top:102px">Products</a>
</div>
<div class="foot-col" style="left:673px">
  <h5>RESOURCES</h5>
  <a href="#pricing" style="top:42px">Pricing</a>
  <a href="#about" style="top:67px">About Us</a>
  <a href="#contact" style="top:90px">Contact Us</a>
</div>
<div class="foot-col" style="left:848px">
  <h5>CONTACT</h5>
  <div class="contact-row" style="top:36px">
    <span class="contact-icon"><svg width="12" height="12" viewBox="0 0 24 24"><path d="M6.6 10.8a15 15 0 0 0 6.6 6.6l2.2-2.2c.3-.3.7-.4 1-.2 1.1.4 2.3.6 3.6.6.6 0 1 .4 1 1V20c0 .6-.4 1-1 1A17 17 0 0 1 3 4c0-.6.4-1 1-1h3.5c.6 0 1 .4 1 1 0 1.3.2 2.5.6 3.6.1.3 0 .7-.2 1z" fill="#fff"/></svg></span>
    <div><small>PHONE NUMBER</small><span>000 000 0000</span></div>
  </div>
  <div class="contact-row" style="top:96px">
    <span class="contact-icon"><svg width="12" height="12" viewBox="0 0 24 24" fill="none" stroke="#fff" stroke-width="2"><rect x="3" y="5" width="18" height="14" rx="2"/><path d="M3 7l9 6 9-6"/></svg></span>
    <div><small>EMAIL US</small><span>hello@lumengrove.example</span></div>
  </div>
</div>

<div class="copyright">Copyright 2024 lumengrove.example</div>

</body>
</html>
```